Clear Meadow Beauty Product Labels for VERITAS certified skin care products

Design a label template for my certified organic skin care products. I need to be able to edit this label for each product.
Packaging will either be white or black (not yet decided) PET boston bottles ranging from 50mL to 500mL sizes (www.kelbrovessels.com.au), 15mL size Tosni PET bottle (www.marlowsupply.com.au)
Types of products include body wash (500mL), body lotion (500mL), facial cleansers (100mL), face and hand creams (50mL), and eye cream (15mL). More products will be developed such as body scrub, shampoo and conditioner.

Target Market(s)

30 - 55 year old women, middle to high income, living on the Northern Rivers NSW Australia

Industry/Entity Type

Cosmetics

Colors

Designer to choose colors to be used in the design.

Requirements
Must have
• Space on front (or middle if rectangular) of label for product name, volume/mass (note: I need to be able to adjust the size of the volume/mass to suit the packaging, also it needs to be at least 2mm from the limits of the package and separate by at least 2mm in all directions from other graphics), VERITAS ORGANIC logo with SVN bud (products will be certified by Southern Verified Natural (SVN) under the VERITAS standard - refer to SVN labelling attached for VERITAS SVN bud), space for marketing message, and my business logo.
• Space on back (or sides if rectangular) for name and address of company (Clear Meadow Beauty, 17 Brennock Road, Lismore Heights NSW 2480), ingredients list, directions for use, claims of product ('x% organic of total', '100% natural ingredients', I need to be able to add claims for each product), storage, batch number and expiry date, space for safety instructions.
Nice to have
• Simple
• Space on front for picture of key ingredient
• Background a neutral colour
• Use of green and brown colours
Should not have
• Too crowded

```html
<!DOCTYPE html>
<html lang="en">
<head>
<meta charset="utf-8">
<title>Clear Meadow Beauty – Label Range</title>
<link rel="stylesheet" href="https://fonts.googleapis.com/css2?family=Josefin+Sans:wght@400;600&family=Roboto:ital,wght@0,400;0,700;1,400&display=swap">
<style>
  :root{
    --paper:#ffffff;
    --label:#ffffff;
    --label-edge:#d9d9d9;
    --leaf:#4c8f3d;
    --bark:#3a0d12;
    --ink:#3b1a1e;
    --ink-soft:#5a3a3d;
    --badge:#6aa84f;
  }
  *{margin:0;padding:0;box-sizing:border-box}
  html,body{width:1200px;height:886px;overflow:hidden;background:var(--paper)}
  .range{position:relative;width:1200px;height:886px}

  .label{position:absolute;background:var(--label);border:1px solid var(--label-edge);display:flex;flex-direction:column;align-items:center;text-align:center;color:var(--ink);font-family:"Roboto",Arial,sans-serif}
  .label__brand{width:100%;background:var(--leaf);display:flex;align-items:center;justify-content:center;gap:6px;color:#fff;font-family:"Josefin Sans",sans-serif;font-weight:600;letter-spacing:.04em;white-space:nowrap}
  .label__brand .dot{border-radius:50%;border:1.5px solid #fff;flex:none}
  .label__strip{width:100%;background:var(--bark);color:#e8d9da;font-size:9px;letter-spacing:.05em;display:flex;align-items:center;justify-content:center}
  .label__kicker{font-size:13px;margin-top:14px}
  .label__name{font-family:"Josefin Sans",sans-serif;font-weight:400;letter-spacing:.01em;line-height:1;white-space:nowrap}
  .label__message{font-style:italic;font-size:8px;color:var(--ink-soft);margin-top:10px;line-height:1.3}
  .label__cert{display:flex;flex-direction:column;align-items:center}
  .badge{width:48px;height:22px;border:1px solid var(--ink-soft);border-radius:2px;display:flex;align-items:center;padding-left:3px;flex:none}
  .badge span{width:15px;height:15px;border-radius:50%;background:var(--badge)}
  .standard{font-weight:700;font-size:12px;line-height:1.1;margin-top:6px}
  .volume{font-weight:700;font-size:12px;margin:12px 0 18px}

  /* body wash */
  .body-wash{left:440px;top:318px;width:212px;height:332px}
  .body-wash .label__brand{height:58px;font-size:14px}
  .body-wash .label__brand .dot{width:13px;height:13px}
  .body-wash .label__strip{height:19px}
  .body-wash .label__kicker{margin-top:42px}
  .body-wash .label__name{font-size:25px;margin-top:6px}
  .body-wash .label__cert{margin-top:44px}

  /* body lotion */
  .body-lotion{left:668px;top:370px;width:198px;height:310px}
  .body-lotion .label__brand{height:50px;font-size:13px}
  .body-lotion .label__brand .dot{width:12px;height:12px}
  .body-lotion .label__strip{height:18px}
  .body-lotion .label__kicker{margin-top:40px}
  .body-lotion .label__name{font-size:21px;margin-top:6px}
  .body-lotion .label__cert{margin-top:40px}

  /* facial cleanser */
  .facial-cleanser{left:884px;top:475px;width:158px;height:210px}
  .facial-cleanser .label__brand{height:32px;font-size:10.5px}
  .facial-cleanser .label__brand .dot{width:10px;height:10px}
  .facial-cleanser .label__strip{height:12px;font-size:7px}
  .facial-cleanser .label__kicker{font-size:10px;margin-top:14px}
  .facial-cleanser .label__name{font-size:17px;margin-top:3px;line-height:1.1}
  .facial-cleanser .label__message{font-size:6px;margin-top:6px}
  .facial-cleanser .label__cert{margin-top:20px}
  .facial-cleanser .badge{width:34px;height:16px}
  .facial-cleanser .badge span{width:11px;height:11px}
  .facial-cleanser .standard{font-size:9px}
  .facial-cleanser .volume{font-size:8px;margin:8px 0 10px}

  /* face cream */
  .face-cream{left:150px;top:595px;width:272px;height:152px}
  .face-cream .label__brand{height:40px;font-size:14px}
  .face-cream .label__brand .dot{width:13px;height:13px}
  .face-cream .label__strip{height:17px;font-size:8px}
  .face-cream .label__kicker{font-size:12px;margin-top:6px}
  .face-cream .label__name{font-size:24px;margin-top:4px}
  .face-cream .label__message{font-size:7px;margin-top:4px}
  .cert-row{display:flex;align-items:center;gap:16px;margin-top:8px}
  .face-cream .standard,.face-cream .volume{font-size:11px;margin:0;line-height:1.1}

  /* eye cream */
  .eye-cream{left:465px;top:713px;width:162px;height:90px}
  .eye-cream .label__brand{height:22px;font-size:10px}
  .eye-cream .label__brand .dot{width:9px;height:9px}
  .eye-cream .label__strip{height:10px;font-size:6px}
  .eye-cream .label__kicker{font-size:8px;margin-top:4px}
  .eye-cream .label__name{font-size:13px;margin-top:2px}
  .eye-cream .label__message{font-size:5px;margin-top:2px}
  .eye-cream .cert-row{gap:8px;margin-top:5px}
  .eye-cream .badge{width:28px;height:12px}
  .eye-cream .badge span{width:8px;height:8px}
  .eye-cream .standard,.eye-cream .volume{font-size:6.5px;margin:0;line-height:1.1}
</style>
</head>
<body>
<main class="range">

  <section class="label body-wash">
    <div class="label__brand"><span class="dot"></span>Clear Meadow Beauty</div>
    <div class="label__strip">LOREM IPSUM DOLOR</div>
    <p class="label__kicker">Lorem Ipsum Dolor</p>
    <h2 class="label__name">BODY WASH</h2>
    <p class="label__message">Lorem ipsum dolor sit amet,<br>consectetuer adipiscin</p>
    <div class="label__cert">
      <div class="badge" role="img" aria-label="Certification badge"><span></span></div>
      <p class="standard">VERITAS<br>ORGANIC</p>
    </div>
    <p class="volume">16 FL OZ/ 500ML</p>
  </section>

  <section class="label body-lotion">
    <div class="label__brand"><span class="dot"></span>Clear Meadow Beauty</div>
    <div class="label__strip">LOREM IPSUM DOLOR</div>
    <p class="label__kicker">Lorem Ipsum Dolor</p>
    <h2 class="label__name">BODY LOTION</h2>
    <p class="label__message">Lorem ipsum dolor sit amet,<br>consectetuer adipiscin</p>
    <div class="label__cert">
      <div class="badge" role="img" aria-label="Certification badge"><span></span></div>
      <p class="standard">VERITAS<br>ORGANIC</p>
    </div>
    <p class="volume">16 FL OZ/ 500ML</p>
  </section>

  <section class="label facial-cleanser">
    <div class="label__brand"><span class="dot"></span>Clear Meadow Beauty</div>
    <div class="label__strip">LOREM IPSUM DOLOR</div>
    <p class="label__kicker">Lorem Ipsum Dolor</p>
    <h2 class="label__name">FACIAL<br>CLEANSER</h2>
    <p class="label__message">Lorem ipsum dolor sit amet,<br>consectetuer adipiscin</p>
    <div class="label__cert">
      <div class="badge" role="img" aria-label="Certification badge"><span></span></div>
      <p class="standard">VERITAS<br>ORGANIC</p>
    </div>
    <p class="volume">16 FL OZ/ 500ML</p>
  </section>

  <section class="label face-cream">
    <div class="label__brand"><span class="dot"></span>Clear Meadow Beauty</div>
    <div class="label__strip">LOREM IPSUM DOLOR</div>
    <p class="label__kicker">Lorem Ipsum Dolor</p>
    <h2 class="label__name">FACE CREAM</h2>
    <p class="label__message">Lorem ipsum dolor sit amet,consectetuer adipiscin</p>
    <div class="cert-row">
      <p class="standard">VERITAS<br>ORGANIC</p>
      <div class="badge" role="img" aria-label="Certification badge"><span></span></div>
      <p class="volume">16 FL OZ<br>500ML</p>
    </div>
  </section>

  <section class="label eye-cream">
    <div class="label__brand"><span class="dot"></span>Clear Meadow Beauty</div>
    <div class="label__strip">LOREM IPSUM DOLOR</div>
    <p class="label__kicker">Lorem Ipsum Dolor</p>
    <h2 class="label__name">EYE CREAM</h2>
    <p class="label__message">Gentle care for delicate eye skin</p>
    <div class="cert-row">
      <p class="standard">VERITAS<br>ORGANIC</p>
      <div class="badge" role="img" aria-label="Certification badge"><span></span></div>
      <p class="volume">16 FL OZ<br>500ML</p>
    </div>
  </section>

</main>
</body>
</html>
```